BPH Business Card 2018

Brellmore Chiropractic. We have two locations that we want to advertise on the same card. Calderwick OrthoAxis campus address: 3815 Pemberly Dr., Suite 240, Flowood, MS 39587. Madison address: 426 Larkmoor Dr., Building D., Madison, MS 39674. website: www.drbrellmore.example. o:(601)555-0148 f:(601)555-0173

Target Market(s)

Health care decision makers: primary care doctors and mothers

Contact Information for Business Card

I have no idea; up for any suggestions and I'd do much better picking from examples versus describing what I'm looking for. We are in a very high end location and would like the cards to look really sharp.

Requirements
Must have
• My name, Tobias R Venmark, D.C.

```html
<!DOCTYPE html>
<html lang="en">
<head>
<meta charset="utf-8">
<title>BPH Business Card 2018</title>
<link rel="stylesheet" href="https://fonts.googleapis.com/css2?family=Cinzel:wght@400&family=Open+Sans:wght@400;600&display=swap">
<style>
  :root {
    --backdrop: #444444;
    --card-light: #f4f4f4;
    --card-dark: #000000;
    --ink: #1a1a1a;
    --ink-reverse: #ffffff;
    --mark-line: #8a8a8a;
  }
  html, body {
    margin: 0;
    padding: 0;
    width: 1200px;
    height: 900px;
    overflow: hidden;
    background: var(--backdrop);
  }
  .stage {
    position: relative;
    width: 1200px;
    height: 900px;
  }
  .card {
    position: absolute;
    top: 200px;
    width: 310px;
    height: 502px;
    box-sizing: border-box;
  }
  .card--front {
    left: 253px;
    background: var(--card-light);
    color: var(--ink);
    border-radius: 52px 0 52px 0;
  }
  .card--back {
    left: 627px;
    background: var(--card-dark);
    color: var(--ink-reverse);
    border-radius: 0 52px 0 52px;
  }
  .brand {
    position: absolute;
    display: flex;
    align-items: center;
    gap: 10px;
  }
  .card--front .brand { left: 30px; top: 108px; }
  .card--back .brand { left: 26px; top: 212px; }
  .brand__dot {
    width: 50px;
    height: 50px;
    border-radius: 50%;
    border: 1.5px solid var(--mark-line);
    flex: none;
  }
  .brand__name {
    font-family: "Cinzel", serif;
    font-weight: 400;
    line-height: 1;
    text-transform: uppercase;
  }
  .brand__line1 { display: block; font-size: 25px; letter-spacing: 0.5px; }
  .brand__line2 { display: block; font-size: 17px; letter-spacing: 0.8px; margin-top: 4px; }
  .holder {
    position: absolute;
    left: 35px;
    top: 234px;
    margin: 0;
    font-family: "Cinzel", serif;
    font-weight: 400;
    font-size: 16px;
    letter-spacing: 0.8px;
    text-transform: uppercase;
  }
  .contact {
    position: absolute;
    left: 33px;
    top: 268px;
    margin: 0;
    padding: 0;
    list-style: none;
    font-family: "Open Sans", sans-serif;
    font-size: 13.5px;
    line-height: 17.5px;
  }
  .contact li { display: flex; align-items: center; gap: 6px; }
  .contact svg { width: 12px; height: 12px; flex: none; fill: var(--ink); }
  .location {
    position: absolute;
    left: 33px;
    margin: 0;
    font-family: "Open Sans", sans-serif;
    font-size: 13.5px;
    line-height: 18px;
  }
  .location--campus { top: 330px; }
  .location--madison { top: 410px; }
  .location__title {
    display: block;
    font-weight: 600;
    text-transform: uppercase;
  }
</style>
</head>
<body>
<main class="stage">
  <section class="card card--front" aria-label="Card front">
    <div class="brand">
      <span class="brand__dot"></span>
      <span class="brand__name">
        <span class="brand__line1">Brellmore</span>
        <span class="brand__line2">Chiropractic</span>
      </span>
    </div>

    <h1 class="holder">Tobias R Venmark, D.C.</h1>

    <ul class="contact">
      <li>
        <svg viewBox="0 0 12 12" aria-hidden="true"><path d="M1 4.5C1 3 3 2 6 2s5 1 5 2.5V5.5H8.5V4.3H3.5V5.5H1z M2.5 6.5h7l1 3.5h-9z"/></svg>
        (601)555-0148
      </li>
      <li>
        <svg viewBox="0 0 12 12" aria-hidden="true"><path d="M3 1h6v3H3z M1 4.5h10v4.5H9V7H3v2H1z M3.5 7.5h5V11h-5z"/></svg>
        (601)555-0173
      </li>
      <li>
        <svg viewBox="0 0 12 12" aria-hidden="true"><circle cx="6" cy="6" r="5"/><path d="M3.5 4.5h2l1 2-1 2M7 3l1.5 1.5" stroke="#f4f4f4" stroke-width="1" fill="none"/></svg>
        www.drbrellmore.example
      </li>
    </ul>

    <p class="location location--campus">
      <span class="location__title">Calderwick OrthoAxis<br>Campus</span>
      3815 Pemberly Dr., Suite 240<br>
      Flowood, MS 39587.
    </p>

    <p class="location location--madison">
      <span class="location__title">Madison</span>
      426 Larkmoor Dr., Building D.,<br>
      Madison, MS 39674.
    </p>
  </section>

  <section class="card card--back" aria-label="Card back">
    <div class="brand">
      <span class="brand__dot"></span>
      <span class="brand__name">
        <span class="brand__line1">Brellmore</span>
        <span class="brand__line2">Chiropractic</span>
      </span>
    </div>
  </section>
</main>
</body>
</html>
```